Gaming Headset Packaging Design

We would like a gaming window box style packaging design for our gaming headset.

We want to use the packaging for 2-3 of our gaming headphone series and hence we would not like to put any product pictures on the packaging.

Size: (enclosed die-cut drawing) please feel free to modify the shape of the window
Material: E Flute Paper box
Type: Window Box style
Design features we prefer: gaming, playful, creative, trendy, High tech.
Requirement: AI file is preferred

Enclosed are a detailed description along with competitor designs and existing die-cut drawing (AI format) for your reference.

Any further questions, please feel free to ask.

```html
<!DOCTYPE html>
<html lang="en">
<head>
<meta charset="utf-8">
<title>Pro Gaming Headset 7.1 – Window Box Dieline</title>
<link rel="stylesheet" href="https://fonts.googleapis.com/css2?family=Barlow+Condensed:ital,wght@0,500;0,600;1,600;1,700&family=Rubik:wght@500;600;800&display=swap">
<style>
  :root {
    --paper: #ffffff;
    --dim-line: #7fc8d8;
    --flap-top: #fdd235;
    --flap-bottom: #fbbd2a;
    --panel-light: #fcd63c;
    --panel-mid: #f9bf2c;
    --panel-deep: #f6a52a;
    --ink: #333333;
    --ink-dark: #262626;
    --charcoal: #2c2c2c;
    --window: #bcbdbf;
    --fold: #c88a20;
    --spec-brown: #9a4f16;
    --spec-text: #8a4a14;
  }
  html, body {
    margin: 0;
    padding: 0;
    width: 1200px;
    height: 977px;
    overflow: hidden;
    background: var(--paper);
  }
  .dieline { display: block; width: 1200px; height: 977px; }
  .dim-line { stroke: var(--dim-line); stroke-width: 1; fill: none; }
  .dim-label { font-family: "Barlow Condensed", sans-serif; font-size: 10px; fill: var(--dim-line); }
  .fold { stroke: var(--fold); stroke-width: 1; stroke-dasharray: 3 3; fill: none; }
  .spec-heading { font-family: "Barlow Condensed", sans-serif; font-weight: 600; font-size: 22px; fill: var(--ink-dark); }
  .spec-list { font-family: "Barlow Condensed", sans-serif; font-weight: 500; font-size: 12px; fill: var(--ink-dark); }
  .product-title { font-family: "Rubik", sans-serif; font-weight: 800; font-size: 43px; fill: var(--ink); letter-spacing: -0.5px; }
  .features-heading { font-family: "Rubik", sans-serif; font-weight: 600; font-size: 18px; fill: var(--ink); }
  .features-list { font-family: "Rubik", sans-serif; font-weight: 500; font-size: 11px; fill: var(--ink); }
  .back-heading { font-family: "Barlow Condensed", sans-serif; font-style: italic; font-weight: 700; font-size: 19px; fill: var(--spec-brown); }
  .back-list { font-family: "Barlow Condensed", sans-serif; font-weight: 500; font-size: 7.6px; fill: var(--spec-text); }
  .back-note { font-family: "Barlow Condensed", sans-serif; font-weight: 500; font-size: 7.8px; fill: var(--spec-text); }
  .back-company { font-family: "Barlow Condensed", sans-serif; font-weight: 600; font-size: 10px; fill: var(--spec-text); }
  .label-box-text { font-family: "Barlow Condensed", sans-serif; font-weight: 500; font-size: 9px; fill: var(--ink-dark); }
</style>
</head>
<body>
<svg class="dieline" viewBox="0 0 1500 1221" xmlns="http://www.w3.org/2000/svg">
  <defs>
    <linearGradient id="flapGradient" x1="0" y1="0" x2="0" y2="1">
      <stop offset="0" stop-color="var(--flap-top)"/>
      <stop offset="1" stop-color="var(--flap-bottom)"/>
    </linearGradient>
    <linearGradient id="flapGradientDown" x1="0" y1="0" x2="0" y2="1">
      <stop offset="0" stop-color="var(--flap-bottom)"/>
      <stop offset="1" stop-color="var(--flap-top)"/>
    </linearGradient>
    <linearGradient id="sidePanelGradient" x1="0" y1="0" x2="1" y2="1">
      <stop offset="0" stop-color="var(--panel-mid)"/>
      <stop offset="0.5" stop-color="var(--panel-deep)"/>
      <stop offset="1" stop-color="var(--panel-mid)"/>
    </linearGradient>
    <linearGradient id="frontPanelGradient" x1="0" y1="0" x2="1" y2="1">
      <stop offset="0" stop-color="var(--panel-light)"/>
      <stop offset="1" stop-color="var(--panel-mid)"/>
    </linearGradient>
    <linearGradient id="backPanelGradient" x1="0" y1="0" x2="1" y2="1">
      <stop offset="0" stop-color="var(--panel-mid)"/>
      <stop offset="0.6" stop-color="var(--panel-deep)"/>
      <stop offset="1" stop-color="var(--panel-mid)"/>
    </linearGradient>
  </defs>

  <!-- Dimension guides -->
  <g class="dimensions">
    <line class="dim-line" x1="160" y1="92" x2="1445" y2="92"/>
    <line class="dim-line" x1="160" y1="85" x2="160" y2="460"/>
    <line class="dim-line" x1="1445" y1="85" x2="1445" y2="470"/>
    <rect x="782" y="85" width="36" height="14" fill="var(--paper)"/>
    <text class="dim-label" x="800" y="95" text-anchor="middle">636.00</text>

    <line class="dim-line" x1="162" y1="117" x2="782" y2="117"/>
    <line class="dim-line" x1="378" y1="110" x2="378" y2="190"/>
    <line class="dim-line" x1="782" y1="110" x2="782" y2="190"/>
    <rect x="252" y="110" width="32" height="14" fill="var(--paper)"/>
    <text class="dim-label" x="268" y="120" text-anchor="middle">108.00</text>
    <rect x="562" y="110" width="32" height="14" fill="var(--paper)"/>
    <text class="dim-label" x="578" y="120" text-anchor="middle">200.00</text>

    <line class="dim-line" x1="82" y1="185" x2="82" y2="1095"/>
    <line class="dim-line" x1="76" y1="185" x2="400" y2="185"/>
    <line class="dim-line" x1="76" y1="1095" x2="165" y2="1095"/>
    <rect x="75" y="625" width="14" height="34" fill="var(--paper)"/>
    <text class="dim-label" transform="translate(86 642) rotate(-90)" text-anchor="middle">450.00</text>

    <line class="dim-line" x1="102" y1="455" x2="102" y2="940"/>
    <line class="dim-line" x1="96" y1="455" x2="165" y2="455"/>
    <line class="dim-line" x1="96" y1="940" x2="165" y2="940"/>
    <rect x="95" y="682" width="14" height="34" fill="var(--paper)"/>
    <text class="dim-label" transform="translate(106 699) rotate(-90)" text-anchor="middle">240.00</text>
  </g>

  <!-- Top flaps -->
  <g class="top-flaps">
    <path d="M163 455 V440 L193 335 H372 V455 Z" fill="url(#flapGradient)"/>
    <path d="M378 455 V238 H382 V203 Q382 187 398 187 H762 Q778 187 778 203 V238 H782 V455 Z" fill="url(#flapGradient)"/>
    <path d="M789 455 V335 H967 L996 440 V455 Z" fill="url(#flapGradient)"/>
    <path d="M1163 455 V423 Q1163 415 1171 415 H1234 Q1242 415 1242 423 V455 Z" fill="url(#flapGradient)"/>
    <path d="M378 238 H402 V242 H540" class="fold" stroke-dasharray="3 2"/>
  </g>

  <!-- Bottom flaps -->
  <g class="bottom-flaps">
    <path d="M163 940 H375 V945 L267 1040 V1095 H171 Q163 1095 163 1087 Z" fill="url(#flapGradientDown)"/>
    <path d="M382 940 H778 V1087 Q778 1095 770 1095 H688 V1050 H473 V1095 H390 Q382 1095 382 1087 Z" fill="url(#flapGradientDown)"/>
    <path d="M785 940 H996 V1087 Q996 1095 988 1095 H893 V1040 L785 945 Z" fill="url(#flapGradientDown)"/>
    <path d="M1003 940 H1405 L1308 1040 V1085 Q1308 1095 1298 1095 H1107 Q1097 1095 1097 1085 V1040 L1003 945 Z" fill="url(#flapGradientDown)"/>
  </g>

  <!-- Glue flap -->
  <path class="glue-flap" d="M1405 455 L1445 467 V928 L1405 940 Z" fill="var(--paper)" stroke="#9a9a9a" stroke-width="1"/>

  <!-- Body panels -->
  <g class="body-panels">
    <rect class="side-panel-left" x="160" y="455" width="218" height="485" fill="url(#sidePanelGradient)" role="img" aria-label="Faceted triangle pattern in yellow and orange"/>
    <rect class="front-panel" x="378" y="455" width="404" height="485" fill="url(#frontPanelGradient)" role="img" aria-label="Faceted triangle pattern in bright yellow"/>
    <rect class="side-panel-right" x="782" y="455" width="218" height="485" fill="url(#frontPanelGradient)" role="img" aria-label="Faceted triangle pattern in bright yellow"/>
    <rect class="back-panel" x="1000" y="455" width="405" height="485" fill="url(#backPanelGradient)" role="img" aria-label="Faceted triangle pattern in yellow and orange"/>
  </g>

  <!-- Front graphic bands -->
  <g class="front-graphic">
    <polygon points="378,485 520,560 378,565" fill="var(--charcoal)"/>
    <polygon points="378,565 520,560 626,620 626,832 430,792 378,772" fill="var(--paper)"/>
    <polygon points="430,792 626,832 626,888 760,888 782,900 782,940 760,940" fill="var(--charcoal)"/>
    <polygon points="880,524 1000,458 1000,524" fill="var(--charcoal)"/>
  </g>

  <!-- Display window -->
  <path class="display-window" d="M695 517 H872 L864 524 H885 L1082 513 L1120 553 V887 H626 V830 L640 812 V705 L626 690 V578 Z" fill="var(--window)"/>

  <!-- Fold lines -->
  <g class="fold-lines">
    <line class="fold" x1="160" y1="455" x2="1405" y2="455"/>
    <line class="fold" x1="160" y1="940" x2="1405" y2="940"/>
    <line class="fold" x1="160" y1="455" x2="160" y2="940"/>
    <line class="fold" x1="378" y1="455" x2="378" y2="940"/>
    <line class="fold" x1="782" y1="455" x2="782" y2="940"/>
    <line class="fold" x1="1000" y1="455" x2="1000" y2="940"/>
    <line class="fold" x1="1405" y1="455" x2="1405" y2="940"/>
    <line x1="1160" y1="495" x2="1242" y2="495" stroke="#8a5a10" stroke-width="1"/>
  </g>

  <!-- Left side panel: specification -->
  <g class="side-specs">
    <text class="spec-heading" x="188" y="547">Specification:</text>
    <g class="spec-list">
      <text x="190" y="571">•</text><text x="206" y="571">Headphone Specification</text>
      <text x="190" y="589">•</text><text x="206" y="589">Speaker Diameter: Ø40mm</text>
      <text x="190" y="607">•</text><text x="206" y="607">Impedance: 32Ω ± 15</text>
      <text x="190" y="626">•</text><text x="206" y="626">Sensitivity S.P.L: 113dB ± 3dB</text>
      <text x="190" y="644">•</text><text x="206" y="644">Rated Power: 20mW</text>
      <text x="190" y="662">•</text><text x="206" y="662">Aggregate capability: 30mW</text>
      <text x="190" y="681">•</text><text x="206" y="681">Frequency Response: 20-20kHz</text>
      <text x="190" y="699">•</text><text x="206" y="699">Plug Type: 3.</text>
      <text x="190" y="717">•</text><text x="206" y="717">Microphone Specification</text>
      <text x="190" y="736">•</text><text x="206" y="736">Microphone Unit: Ø6 x 5mm</text>
      <text x="190" y="754">•</text><text x="206" y="754">Sensitivity S.P.L 34dB ± 3dB</text>
      <text x="190" y="772">•</text><text x="206" y="772">Impedance: &lt;2.2k</text>
      <text x="190" y="791">•</text><text x="206" y="791">Frequency Response: 30-16kHz</text>
      <text x="190" y="809">•</text><text x="206" y="809">Standard Operating Voltage: 4.5V</text>
      <text x="190" y="827">•</text><text x="206" y="827">S/N Ratio: ≥ 60dB</text>
      <text x="190" y="846">•</text><text x="206" y="846">Plug Type: 3.5mm Stereo5mm Stereo</text>
    </g>
  </g>

  <!-- Front panel: title and features -->
  <g class="front-copy">
    <text class="product-title" x="402" y="637">PRO</text>
    <text class="product-title" x="402" y="681">GAMING</text>
    <text class="product-title" x="402" y="725">HEADSET</text>
    <text class="product-title" x="402" y="769">7.1</text>
    <text class="features-heading" x="403" y="842">FEATURES:</text>
    <g class="features-list">
      <text x="404" y="864">● Virtual 7.1 Surround Sound</text>
      <text x="404" y="877">● Dual Drivers on each ear for Accuracy</text>
      <text x="404" y="890">● 3D Sound Vibration</text>
      <text x="404" y="903">● Bendable Stainless-Steel headband</text>
      <text x="404" y="916">● Soft and soothing earpads</text>
    </g>
  </g>

  <!-- Back panel: information block -->
  <g class="back-info">
    <rect x="1127" y="524" width="258" height="338" fill="#ffffff" fill-opacity="0.38"/>
    <text class="back-heading" x="1141" y="558">Specification:</text>
    <g class="back-list">
      <text x="1143" y="576">•  Headphone Specification</text>
      <text x="1143" y="586">•  Speaker Diameter: Ø40mm</text>
      <text x="1143" y="596">•  Impedance: 32Ω ± 15</text>
      <text x="1143" y="607">•  Sensitivity S.P.L: 113dB ± 3dB</text>
      <text x="1143" y="617">•  Rated Power: 20mW</text>
      <text x="1143" y="627">•  Aggregate capability: 30mW</text>
      <text x="1143" y="638">•  Frequency Response: 20-20kHz</text>
      <text x="1143" y="648">•  Plug Type: 3.5mm Stereo</text>
      <text x="1259" y="576">•  Microphone Specification</text>
      <text x="1259" y="586">•  Microphone Unit: Ø6 x 5mm</text>
      <text x="1259" y="596">•  Sensitivity S.P.L 34dB ± 3dB</text>
      <text x="1259" y="607">•  Impedance: &lt;2.2k</text>
      <text x="1259" y="617">•  Frequency Response: 30-16kHz</text>
      <text x="1259" y="627">•  Standard Operating Voltage: 4.5V</text>
      <text x="1259" y="638">•  S/N Ratio: ≥ 60dB</text>
      <text x="1259" y="648">•  Plug Type: 3.5mm Stereo</text>
    </g>
    <g class="back-note">
      <text x="1141" y="674">Warning: Adjust headphone's sound to a proper volume. Loud sound may</text>
      <text x="1141" y="684">damage your ears. For traffic safety never use the headset while driving.</text>
      <text x="1141" y="705">Caution: If the user attempts to inspect or modify the product in any way</text>
      <text x="1141" y="715">we don't guarantee the performance of the product. Specifications and</text>
      <text x="1141" y="725">design are subject to possible modification notice due to improvements.</text>
      <text x="1141" y="746">Once specific place to be left for Bar Code, manufacturer information</text>
      <text x="1141" y="756">and Certificate Symbols (Picture for reference)</text>
    </g>
    <text class="back-company" x="1141" y="778">COMPANY NAME HERE</text>
    <g class="back-note">
      <text x="1141" y="791">Lorem ipsum dolor sit amet, consectetuer adipiscing elit, sed diam</text>
      <text x="1141" y="801">nonummy nibh euismod tincidunt ut laoreet dolore magna aliquam erat</text>
      <text x="1141" y="811">volutpat. Ut wisi enim ad minim veniam, quis nostrud exerci tation</text>
      <text x="1141" y="822">ullamcorper suscipit lobortis nisl ut aliquip ex ea commodo consequat.</text>
      <text x="1141" y="832">Duis autem vel eum iriure dolor in hendrerit in vulputate velit esse</text>
      <text x="1141" y="842">molestie consequat, vel illum dolore eu feugiat nulla facilisis</text>
    </g>
    <rect x="1138" y="872" width="139" height="47" fill="var(--paper)"/>
    <text class="label-box-text" x="1207" y="898" text-anchor="middle">ICONS</text>
    <rect x="1284" y="872" width="95" height="47" fill="var(--paper)"/>
    <text class="label-box-text" x="1331" y="898" text-anchor="middle">barcode</text>
  </g>
</svg>
</body>
</html>
```